Pathways to Brightmoor Land Ventures

size of the ad - 8”x 10.75" plus 0.25" bleed
I would like an ad for a magazine that will stand out and make people want to read the ad.
The ad should not be crowded and people reading the ad will be able to read the text.
I would like it to be a creative and modern-day design.
the list of topics should not be the focus of the ad.
the text is attached.
If you decide to use people in the ad then please no ladies.
please note that leave over 1 inch for the bottom of the footer

```html
<!DOCTYPE html>
<html lang="en">
<head>
<meta charset="UTF-8">
<title>Real Estate Course – Magazine Ad</title>
<link rel="stylesheet" href="https://fonts.googleapis.com/css2?family=Poppins:wght@400;500;600;700;800;900&display=swap">
<style>
  :root {
    --navy-deep: #0d2a52;
    --navy: #143a6b;
    --navy-bar: #0f3463;
    --blue-bright: #2a8be8;
    --blue-mid: #1f76d2;
    --blue-accent: #2187e6;
    --ink: #1b1b1f;
    --ink-soft: #2e3138;
    --white: #ffffff;
    --canvas: #eef1f5;
    --dash: #4a5a78;
  }
  * { box-sizing: border-box; margin: 0; padding: 0; }
  html, body {
    width: 1200px; height: 2400px; overflow: hidden;
    background: var(--canvas);
    font-family: "Poppins", sans-serif;
  }
  .flyer {
    position: absolute; left: 40px; top: 453px;
    width: 1120px; height: 1494px;
    background: var(--white);
    box-shadow: 0 18px 50px rgba(20, 40, 70, 0.18);
    overflow: hidden;
  }
  .hero {
    position: absolute; left: 0; top: 0; width: 1120px; height: 622px;
    background: linear-gradient(135deg, var(--navy-deep) 0%, var(--navy) 100%);
  }
  .hero-photo {
    position: absolute; right: 0; top: 0; width: 620px; height: 622px;
    background:
      radial-gradient(ellipse at 62% 58%, rgba(140,150,165,0.55) 0%, rgba(60,80,110,0.35) 35%, rgba(20,50,90,0) 70%),
      linear-gradient(90deg, rgba(20,58,107,0) 0%, #1d3f6c 40%, #233f62 100%);
  }
  .hero-title { position: absolute; left: 55px; top: 0; width: 580px; height: 622px; }
  .hero-title text { font-family: "Poppins", sans-serif; font-weight: 800; }

  .band { position: absolute; top: 622px; height: 250px; }
  .band--left { left: 0; width: 538px; background: var(--blue-bright); }
  .band--right { left: 538px; width: 582px; background: var(--blue-mid); }
  .band-text {
    position: absolute; color: var(--white);
    font-weight: 800; text-transform: uppercase;
    line-height: 1.08; white-space: nowrap;
  }
  .band--left .band-text { left: 68px; top: 46px; font-size: 40px; }
  .band--right .band-text { left: 47px; top: 34px; font-size: 41px; line-height: 1.1; }

  .session-box {
    position: absolute; left: 68px; top: 909px; width: 970px; height: 66px;
    display: flex;
  }
  .session-box .cell {
    border: 2px dashed var(--dash); border-radius: 4px;
    display: flex; align-items: center; justify-content: center;
    color: var(--ink); font-weight: 800; font-size: 44px; letter-spacing: 0.5px;
    line-height: 1; white-space: nowrap;
  }
  .cell--place { width: 300px; }
  .cell--date { flex: 1; margin-left: -2px; font-size: 42px; }

  .perks {
    position: absolute; top: 993px; left: 68px; width: 970px; height: 36px;
  }
  .perk {
    position: absolute; top: 0; display: flex; align-items: center; gap: 8px;
    font-weight: 600; font-size: 26px; color: var(--ink); white-space: nowrap;
  }
  .perk svg { width: 26px; height: 26px; flex: none; }
  .perk--sessions { left: 0; }
  .perk--scholarship { left: 537px; }

  .early-bird {
    position: absolute; left: 53px; top: 1053px;
    font-weight: 800; line-height: 0.92; text-transform: uppercase;
  }
  .early-bird .line1 { display: block; color: var(--blue-accent); font-size: 33px; letter-spacing: 0.5px; }
  .early-bird .line2 { display: block; color: var(--navy); font-size: 46px; }
  .audience-bar {
    position: absolute; left: 270px; top: 1053px; width: 769px; height: 79px;
    background: var(--navy-bar); border-radius: 8px;
    color: var(--white); font-weight: 700; font-size: 28px; line-height: 1.1;
    padding: 12px 0 0 28px; text-transform: uppercase;
  }

  .topics-heading {
    position: absolute; left: 53px; top: 1166px;
    font-weight: 700; font-size: 29px; color: var(--ink); text-transform: uppercase;
  }
  .topics-heading .label { color: var(--blue-accent); }
  .topic-list { position: absolute; top: 1215px; list-style: none; }
  .topic-list li {
    display: flex; align-items: center; gap: 8px; white-space: nowrap;
    font-weight: 500; font-size: 19px; color: var(--ink-soft); line-height: 23px;
  }
  .topic-list svg { width: 13px; height: 13px; flex: none; }
  .topic-list--a { left: 53px; }
  .topic-list--b { left: 440px; }
  .topic-list--c { left: 775px; top: 1218px; }
</style>
</head>
<body>
  <svg width="0" height="0" style="position:absolute">
    <defs>
      <symbol id="tick-badge" viewBox="0 0 24 24">
        <circle cx="12" cy="12" r="11" fill="#2187e6"/>
        <path d="M7 12.4l3.2 3.1L17 8.8" fill="none" stroke="#fff" stroke-width="2.4" stroke-linecap="round" stroke-linejoin="round"/>
      </symbol>
      <symbol id="tick-small" viewBox="0 0 24 24">
        <circle cx="12" cy="12" r="10" fill="none" stroke="#2187e6" stroke-width="2"/>
        <path d="M7.5 12.3l3 2.9 6-6.2" fill="none" stroke="#2187e6" stroke-width="2.2" stroke-linecap="round" stroke-linejoin="round"/>
      </symbol>
    </defs>
  </svg>

  <main class="flyer">
    <section class="hero">
      <div class="hero-photo" role="img" aria-label="Businessman in a dark suit holding a miniature city skyline between his hands"></div>
      <svg class="hero-title" viewBox="0 0 580 622" aria-label="Real Estate Course">
        <text x="0" y="275" font-size="226" fill="#2187e6" textLength="562" lengthAdjust="spacingAndGlyphs">REAL</text>
        <text x="0" y="410" font-size="166" fill="#ffffff" textLength="562" lengthAdjust="spacingAndGlyphs">ESTATE</text>
        <text x="-4" y="530" font-size="158" fill="#ffffff" textLength="566" lengthAdjust="spacingAndGlyphs">COURSE</text>
      </svg>
    </section>

    <section class="band band--left">
      <p class="band-text">Pathways to<br>Brightmoor Land<br>Ventures</p>
    </section>
    <section class="band band--right">
      <p class="band-text">Investing in<br>knowledge is<br>investing<br>inopportunities.</p>
    </section>

    <div class="session-box">
      <div class="cell cell--place">OAKRIDGE</div>
      <div class="cell cell--date">STARTING FEBRUARY 28TH</div>
    </div>

    <div class="perks">
      <div class="perk perk--sessions"><svg><use href="#tick-badge"/></svg>10 -Tuesday evenings sessions</div>
      <div class="perk perk--scholarship"><svg><use href="#tick-badge"/></svg>Limited Partial Scholarships</div>
    </div>

    <div class="early-bird"><span class="line1">Early Bird</span><span class="line2">Special</span></div>
    <div class="audience-bar">For those that started or would like to<br>go into real estate</div>

    <h2 class="topics-heading"><span class="label">Topics:</span> Partial Listing</h2>
    <ul class="topic-list topic-list--a">
      <li><svg><use href="#tick-small"/></svg>Real estate investment strategies</li>
      <li><svg><use href="#tick-small"/></svg>Due diligence</li>
      <li><svg><use href="#tick-small"/></svg>Financing</li>
      <li><svg><use href="#tick-small"/></svg>Underwriting</li>
    </ul>
    <ul class="topic-list topic-list--b">
      <li><svg><use href="#tick-small"/></svg>Property management</li>
      <li><svg><use href="#tick-small"/></svg>Real estate Legal basics</li>
      <li><svg><use href="#tick-small"/></svg>Sourcing deals</li>
    </ul>
    <ul class="topic-list topic-list--c">
      <li><svg><use href="#tick-small"/></svg>Syndication</li>
      <li><svg><use href="#tick-small"/></svg>Dealing with brokers</li>
      <li><svg><use href="#tick-small"/></svg>Tax fundamentals</li>
    </ul>
  </main>
</body>
</html>
```